Home page web design for "Tales from Tamsin"

We need a home page web design for a start up company that will write memoirs for seniors.
The completed project will need to include PSD files...NO HTML or CSS necessary.
Attached is a brief outline concept that may give you some ideas...but you are the creative professionals, so please feel free to add your ideas. We will also attach some files that show you our logo, brochures, and photos that could be used to give you ideas of our focus.
There will need to be access to the other pages on the home page to include: 'About Us'; 'How We Can Help'; 'Community Sessions'; 'Senior Consulting ' and 'Contact Us'.
Updates

Project Deadline Extended Reason: We want designers to have sufficient time to get all their proposals and revisions submitted. THANK YOU Added Wednesday, October 15, 2014

Target Market(s)

Seniors and Baby Boomers

Industry/Entity Type

It Company

Number of Pages Required

1 page

Colors
f9ba93
fbca95
faa54b
faf289
f37123

Requirements
Must have
• Script easy on senior eyes.
• Initial contact number would be 844-4LEGACY
Nice to have
• While the color pallet is non-specific we prefer the warm colors.
• salmon, peach.......
• NOT so much the orange of Halloween:)
• However, please utilize your creativity and put in colors you feel will draw best with your design.

```html
<!DOCTYPE html>
<html lang="en">
<head>
<meta charset="utf-8">
<title>Tales from Tamsin — Home</title>
<link href="https://fonts.googleapis.com/css2?family=Arimo:ital,wght@1,700&family=Lato:ital,wght@0,400;1,400&family=Roboto:wght@400;500;700&display=swap" rel="stylesheet">
<style>
  :root {
    --page-orange: #de7d4c;
    --nav-top: #2a2a2a;
    --nav-bottom: #050505;
    --white: #ffffff;
    --ink: #1a1008;
    --gold: #a88a2c;
    --btn-primary: #f37123;
    --btn-secondary: #fbca95;
    --rule: #b0623a;
    --photo-a: #6b3a34;
    --photo-b: #c98a7c;
    --photo-c: #e9c4b4;
  }
  * { box-sizing: border-box; margin: 0; padding: 0; }
  html, body { width: 1200px; height: 870px; overflow: hidden; }
  body {
    position: relative;
    background: linear-gradient(160deg, #e2844f 0%, var(--page-orange) 55%, #d6753f 100%);
    font-family: "Lato", sans-serif;
    color: var(--ink);
  }
  .hero-photo {
    position: absolute; left: 0; top: 0; width: 540px; height: 870px;
    clip-path: polygon(0 0, 492px 0, 538px 870px, 0 870px);
    background: linear-gradient(120deg, var(--photo-c) 0%, var(--photo-b) 35%, var(--photo-a) 70%, #8a4f44 100%);
  }
  .nav-bar {
    position: absolute; left: 325px; top: 51px; width: 875px; height: 59px;
    background: linear-gradient(var(--nav-top), var(--nav-bottom));
  }
  .nav-link {
    position: absolute; top: 73px;
    font-family: "Roboto", sans-serif; font-weight: 500; font-size: 15.5px;
    color: var(--white); text-decoration: none; white-space: nowrap;
  }
  .logo-badge {
    position: absolute; left: 76px; top: 19px; width: 265px; height: 127px;
    border-radius: 50%; background: var(--white);
    display: flex; align-items: center; justify-content: center;
    font-family: "Lato", sans-serif; font-size: 25px; color: var(--gold);
  }
  .call-box {
    position: absolute; left: 1041px; top: 10px;
    font-family: "Roboto", sans-serif; color: var(--white);
  }
  .call-box svg { position: absolute; left: -24px; top: 6px; }
  .call-label { font-size: 10px; display: block; }
  .call-number { font-size: 16.5px; font-weight: 700; display: block; margin-top: -1px; }
  .corner-ornament {
    position: absolute; background: rgba(150, 70, 30, 0.35); border-radius: 6px;
  }
  .headline {
    position: absolute; left: 559px; top: 194px;
    font-family: "Arimo", sans-serif; font-style: italic; font-weight: 700;
    font-size: 33px; line-height: 39px; color: var(--white);
  }
  .subhead {
    position: absolute; left: 562px; top: 279px;
    font-style: italic; font-size: 21px; font-weight: 400;
  }
  .body-copy {
    position: absolute; left: 563px; top: 315px; width: 608px;
    font-size: 14.4px; line-height: 17.6px; letter-spacing: 0.45px;
  }
  .body-copy p { margin-bottom: 18.5px; }
  .body-copy p.lead { margin-bottom: 12px; letter-spacing: 1.05px; }
  .btn {
    position: absolute; top: 737px; width: 161px; height: 43px;
    border: 2px solid var(--white); border-radius: 22px;
    font-family: "Roboto", sans-serif; font-weight: 700; font-size: 16px;
    display: flex; align-items: center; justify-content: center;
    color: var(--ink); text-decoration: none;
  }
  .btn-gift { left: 564px; background: var(--btn-primary); }
  .btn-learn { left: 748px; background: var(--btn-secondary); }
  .footer-rule {
    position: absolute; left: 557px; top: 818px; width: 617px; height: 1px;
    background: var(--rule);
  }
  .copyright {
    position: absolute; right: 34px; top: 832px;
    font-family: "Roboto", sans-serif; font-size: 13.5px; color: #2a160c;
  }
  .photo-circle {
    position: absolute; top: 650px; width: 196px; height: 196px;
    border-radius: 50%; border: 4px solid var(--white);
  }
  .circle-sunset { left: 99px; background: linear-gradient(#f0a24a, #c05a2c 55%, #3d2a2a); }
  .circle-grandpa { left: 316px; background: linear-gradient(135deg, #f2f2f4, #c9d6e6 50%, #3c5a8a); }
</style>
</head>
<body>
  <div class="hero-photo" role="img" aria-label="Photo of an elderly woman writing her memoirs in a book at a desk"></div>

  <nav class="nav-bar" aria-label="Main"></nav>
  <a class="nav-link" href="#" style="left:357px">HOME</a>
  <a class="nav-link" href="#" style="left:420px">ABOUT US</a>
  <a class="nav-link" href="#" style="left:512px">HOW WE CAN HELP</a>
  <a class="nav-link" href="#" style="left:677px">COMMUNITY SERVICES</a>
  <a class="nav-link" href="#" style="left:863px">SENIOR CONSULTING</a>
  <a class="nav-link" href="#" style="left:1050px">CONTACT US</a>

  <div class="logo-badge">Tales from Tamsin</div>

  <div class="call-box">
    <svg width="20" height="20" viewBox="0 0 24 24" aria-hidden="true"><path fill="#fff" d="M6.6 10.8a15.2 15.2 0 0 0 6.6 6.6l2.2-2.2a1 1 0 0 1 1-.25 11.4 11.4 0 0 0 3.6.57 1 1 0 0 1 1 1V20a1 1 0 0 1-1 1A17 17 0 0 1 3 4a1 1 0 0 1 1-1h3.5a1 1 0 0 1 1 1c0 1.25.2 2.45.57 3.57a1 1 0 0 1-.25 1z"/></svg>
    <span class="call-label">CALL US NOW!</span>
    <span class="call-number">844-4LEGACY</span>
  </div>

  <div class="corner-ornament" role="img" aria-label="Decorative corner flourish" style="left:514px;top:132px;width:96px;height:92px"></div>
  <div class="corner-ornament" role="img" aria-label="Decorative corner flourish" style="left:1078px;top:710px;width:96px;height:92px"></div>

  <h1 class="headline">Ordinary Lives……<br>Extraordinary Legacies</h1>
  <h2 class="subhead">When a genealogy doesn’t say enough!</h2>

  <div class="body-copy">
    <p class="lead">If you were alive in 100 years, what would you share with your descendants? Now you have a vehicle to help you immortalize your thoughts for the future…specifically for those who will want to know!</p>
    <p>We are not all presidents of countries or CEO’s of fortune 500 companies! But “every life legacy is a gift to be treasured by the next generation.”</p>
    <p>Does your family host generations of soldiers, doctors, farmers, scientists, mechanics, entrepreneurs, writers, politicians, contractors, pastors, artisans, athletes, musicians, etc..? Generational patterns can often emerge when writing your story that will interest the next generation.</p>
    <p>A genealogy, while very relevant, doesn’t offer the personal story of the names we find. A biography can place a deeper relevance on the face for future descendants. Every life is a legacy to pass forward and we at Tales from Tamsin believe everyone should chronicle their life journey in writing. This commitment allows you to be remembered for who you truly are as a person.</p>
    <p>Think about it….<br>Do you know the triumphs and tribulations of your ancestors?<br>Do you wish you did?<br>Well, so will those falling into your personal family tree.</p>
  </div>

  <a class="btn btn-gift" href="#">GREAT GIFT IDEA</a>
  <a class="btn btn-learn" href="#">LEARN MORE</a>

  <div class="photo-circle circle-sunset" role="img" aria-label="Photo of an older couple walking on a beach at sunset"></div>
  <div class="photo-circle circle-grandpa" role="img" aria-label="Photo of a grandfather reading a book with his grandchild"></div>

  <div class="footer-rule"></div>
  <p class="copyright">Copyright 2014, <strong>Tales from Tamsin</strong>. All Rights Reserved</p>
</body>
</html>
```